Stylish Business Cards Wanted

- DOUBLE SIDED Design Required -

High end, edgy cards for a corporate and personal stylist. Must include logo,
Name: Belinda Forsey
Title: Director and Stylist
telephone : +61 8 8217 4592
email: belinda@thegarbledger.example
website: thegarbledger.example
Tag: Corporate Workwear & Uniform Specialist | Personal Stylist
Would like nice icons for telephone, email, website

Target Market(s)

Businesses wanting stylish uniforms, people wanting stylish wardrobes

Industry/Entity Type

Corporate Workwear Stylist

Contact Information for Business Card

I would like black, white and gold foiling incorporated in the design - possibly a touch of the other colours on my branding guide attached Name: Belinda Forsey Title: Director and Stylist telephone : +61 8 8217 4592 email: belinda@thegarbledger.example website: thegarbledger.example Tag: Corporate Workwear & Uniform Specialist | Personal Stylist Would like nice icons for telephone, email, website

Font styles to use
Other font styles liked:
• Raleway

Colors

Designer to choose colors to be used in the design.

Requirements
Must have
• Gold foil accents

```html
<!DOCTYPE html>
<html lang="en">
<head>
<meta charset="utf-8">
<title>The Garb Ledger – Business Cards</title>
<link rel="stylesheet" href="https://fonts.googleapis.com/css2?family=Raleway:wght@400;500;700&family=Dancing+Script:wght@400;600&display=swap">
<style>
  :root {
    --backdrop: #c9c9c9;
    --navy: #141b33;
    --gold: #e1b552;
    --white: #ffffff;
    --pink: #d8126f;
  }
  * { margin: 0; padding: 0; box-sizing: border-box; }
  html, body { width: 1200px; height: 852px; overflow: hidden; }
  body { background: var(--backdrop); position: relative; font-family: "Raleway", sans-serif; }

  .card {
    position: absolute;
    width: 520px;
    height: 300px;
    background: var(--navy);
    border-radius: 22px;
    overflow: hidden;
  }
  .card--front { left: 70px; top: 110px; }
  .card--back  { left: 610px; top: 440px; }

  .wordmark {
    font-family: "Raleway", sans-serif;
    font-weight: 700;
    text-transform: uppercase;
    letter-spacing: 0.08em;
    line-height: 1.1;
  }
  .card--front .wordmark {
    position: absolute; left: 0; right: 0; top: 50%;
    transform: translateY(-50%);
    text-align: center;
    font-size: 40px;
    color: var(--gold);
  }
  .card--back .wordmark {
    position: absolute; left: 38px; top: 86px;
    font-size: 30px;
    color: var(--white);
  }

  .tagline {
    position: absolute; right: 34px; top: 34px;
    text-align: right;
    font-family: "Dancing Script", cursive;
    font-weight: 400;
    font-size: 17px;
    line-height: 1.25;
    color: var(--white);
  }
  .tagline li { list-style: none; position: relative; padding-right: 12px; }
  .tagline li::after {
    content: ""; position: absolute; right: 0; top: 8px;
    width: 5px; height: 5px; border-radius: 50%; background: var(--pink);
  }

  .contact {
    position: absolute; left: 298px; top: 142px;
    list-style: none;
    font-size: 12.5px; line-height: 16px; color: var(--white);
  }
  .contact li { display: flex; align-items: center; gap: 9px; margin-bottom: 5px; }
  .contact li:last-child { margin-bottom: 0; }
  .contact svg { width: 13px; height: 13px; flex: none; }

  .band { position: absolute; left: 0; top: 0; }

  .social {
    position: absolute; right: 26px; top: 248px;
    display: flex; align-items: center; gap: 7px;
    font-size: 13px; font-weight: 500; color: var(--navy);
  }
  .social__dot { width: 10px; height: 10px; border-radius: 50%; background: var(--navy); }

  .person { position: absolute; left: 38px; top: 218px; }
  .person__name { font-family: "Dancing Script", cursive; font-weight: 600; font-size: 28px; line-height: 1; color: var(--gold); }
  .person__title { font-size: 13px; color: var(--white); margin-top: 4px; }
</style>
</head>
<body>

  <section class="card card--front" aria-label="Card front">
    <div class="wordmark">The Garb Ledger</div>
  </section>

  <section class="card card--back" aria-label="Card back">
    <svg class="band" width="520" height="300" viewBox="0 0 520 300" aria-hidden="true">
      <polygon points="0,300 0,292 300,252 300,300" fill="var(--pink)"/>
      <polygon points="302,226 520,226 520,300 290,300" fill="var(--gold)"/>
    </svg>

    <div class="wordmark">The Garb<br>Ledger</div>

    <ul class="tagline">
      <li>Corporate Workwear</li>
      <li>&amp; Uniform Specialist</li>
      <li>Personal Stylist</li>
    </ul>

    <ul class="contact">
      <li>
        <svg viewBox="0 0 16 16"><circle cx="8" cy="8" r="7.5" fill="var(--gold)"/><path d="M5.2 4.2l1.6 1.6-.9 1.1c.6 1.2 1.5 2.1 2.7 2.7l1.1-.9 1.6 1.6-1 1.2C7.6 11.3 4.7 8.4 4 5.2z" fill="var(--navy)"/></svg>
        +61 8 8217 4592
      </li>
      <li>
        <svg viewBox="0 0 16 16"><rect x="1" y="3.5" width="14" height="9" rx="1" fill="none" stroke="var(--gold)" stroke-width="1.4"/><path d="M1.5 4l6.5 5 6.5-5" fill="none" stroke="var(--gold)" stroke-width="1.4"/></svg>
        belinda@thegarbledger.example
      </li>
      <li>
        <svg viewBox="0 0 16 16"><circle cx="8" cy="8" r="7.5" fill="var(--gold)"/><path d="M0.5 8h15M8 .5c-3 3-3 12 0 15M8 .5c3 3 3 12 0 15" fill="none" stroke="var(--navy)" stroke-width="1"/></svg>
        www.thegarbledger.example
      </li>
    </ul>

    <div class="social">
      <span class="social__dot"></span>
      /thegarbledger101
    </div>

    <div class="person">
      <div class="person__name">Belinda Forsey</div>
      <div class="person__title">Director and Stylist</div>
    </div>
  </section>

</body>
</html>
```